Book Cover Design - Rooted Together: 7 Paths to Raise a Home that Flourishes

International cover needed for the Australian (Marlow Fenwick/QRT Press 2011) non-fiction book Rooted Together: 7 Paths to Raise a Home that Flourishes.

Blurb: With the birth of a baby, come other new beginnings, the birth of a mother, of a father, and of a family. With each stage of a child's growth, and with every new baby, there are more new beginnings. In older cultures and in villages around the world, parenthood was considered a rite of passage but traditions that guided parents into becoming a family have largely been lost - until now.

This ground breaking book walks a new generation of mothers and fathers through the eight steps of the modern parenthood rite of passage, from couple-connection to family-foundations, so they can prepare for and continue to grow a family that thrives.

Bio: Mara Quinlan is a relationship counsellor, parent educator and columnist for Sensible Homelife magazine. She lives in Sydney with her husband, their three gorgeous children and an itinerary of pets. This is her first book.
Updates

Thank you for your patience, I haven't ever done anything like this before and the designs submitted have helped me to be more specific in my requests. Please see the updated brief. The most important point is that I am seeking a TEXT based cover, so BOTH the TITLE and SUBTITLE should take up most of the space, the image could either be in the background with the title and subtitle overlayed, or be much smaller to fit around them. I have attached some more images to the brief, hope they help to convey the 'feel' I am after.  Thanks again!

Reason: Thank you so much for taking an interest in this project, the process has been very educational and helpful for me. While some of the stock art in the submitted designs are great, I've decided to commission a custom illustration which completely captures the meaning of Rooted Together. I will upload the illustration once it's complete for designers who are still interested to use. Thank you for your patience! Mara

Thank you all for your patience and for opening up my thinking about what I am really hoping for with this cover. I have uploaded some new tree designs and more specific instructions that I would like to be included in the cover design. I'm looking forward to seeing your creations!

With warm regards,

Mara

Target Market(s)

Couples thinking about having a baby and new parents of one or more young children.

Industry/Entity Type

Baby

Requirements
Must have
• TEXT based cover with BOTH the TITLE and SUBTITLE taking up most of the page.
Colors to match the Australian version (see attached)
Tree design bottom left (as per Trunk Treatment image attached) OR Heart Tree Design
Root design (as per one of the two images attached)
PLEASE ADD: three new shoots coming up from the ground under the tree to symbolize the children.
Nice to have
• Artistic effect to complement Australian cover.
Subtle retro feel to complement Australian cover.
Should not have
• The book is inclusive of all parents (including same-sex parents) so no images of mother/father and baby.

```html
<!DOCTYPE html>
<html lang="en">
<head>
<meta charset="utf-8">
<title>Rooted Together — Book Cover</title>
<link rel="stylesheet" href="https://fonts.googleapis.com/css2?family=Poiret+One&family=Varela+Round&display=swap">
<style>
  :root {
    --sky: #bfe2e1;
    --sky-deep: #afd9d8;
    --bark: #7b5a3b;
    --leaf: #4f9a3f;
    --leaf-light: #a3cd5e;
    --leaf-mid: #7fb64a;
    --sunset: #ef8a32;
    --ribbon: #e8873a;
    --ribbon-dark: #c8692a;
    --ribbon-fold: #6e2a1e;
    --cream: #fff8ee;
    --rule: rgba(90, 120, 120, 0.3);
  }
  * { margin: 0; padding: 0; box-sizing: border-box; }
  html, body { width: 807px; height: 1200px; overflow: hidden; }
  body {
    background: var(--sky);
    font-family: "Poiret One", "Josefin Sans", sans-serif;
  }
  .cover {
    position: relative;
    width: 807px;
    height: 1200px;
    background: radial-gradient(ellipse at 50% 40%, #c6e6e4 0%, var(--sky) 60%, var(--sky-deep) 100%);
    overflow: hidden;
  }
  .tree-art {
    position: absolute;
    left: 180px;
    top: 38px;
    width: 460px;
    height: 420px;
    border-radius: 8px;
    background: linear-gradient(160deg, var(--leaf-light) 0%, var(--leaf-mid) 60%, #6f9a48 100%);
  }
  .title-ribbon {
    position: absolute;
    left: 90px;
    top: 425px;
    width: 630px;
    height: 150px;
  }
  .title-ribbon svg { position: absolute; inset: 0; }
  .title-ribbon h1 {
    position: absolute;
    left: 60px;
    right: 60px;
    top: 26px;
    text-align: center;
    font-family: "Varela Round", "Nunito", sans-serif;
    font-weight: 400;
    font-size: 54px;
    line-height: 1.1;
    color: var(--cream);
    text-shadow: 0 2px 3px rgba(120, 60, 20, 0.45);
  }
  .rule {
    position: absolute;
    left: 110px;
    width: 590px;
    height: 2px;
    background: radial-gradient(ellipse at center, var(--rule) 0%, transparent 75%);
  }
  .rule--top { top: 602px; }
  .rule--bottom { top: 1026px; }
  .subtitle { text-transform: uppercase; font-weight: 400; }
  .subtitle span {
    position: absolute;
    left: 0;
    right: 0;
    text-align: center;
    line-height: 1;
    white-space: nowrap;
  }
  .subtitle .count { top: 632px; font-size: 90px; color: var(--bark); letter-spacing: 3px; }
  .subtitle .verb { top: 704px; font-size: 122px; color: var(--bark); letter-spacing: 2px; }
  .subtitle .verb em { font-style: normal; color: var(--leaf); }
  .subtitle .object { top: 818px; font-size: 68px; color: var(--bark); letter-spacing: 2px; }
  .subtitle .outcome { top: 884px; font-size: 140px; color: var(--sunset); letter-spacing: 1px; }
  .author {
    position: absolute;
    left: 0;
    right: 0;
    top: 1118px;
    text-align: center;
    font-size: 44px;
    line-height: 1;
    color: var(--bark);
    letter-spacing: 3px;
    text-transform: uppercase;
    -webkit-text-stroke: 0.6px var(--bark);
  }
</style>
</head>
<body>
  <main class="cover">
    <div class="tree-art" role="img" aria-label="Illustration of a tree with a brown trunk and a round canopy of green leaves"></div>

    <div class="title-ribbon">
      <svg width="630" height="150" viewBox="0 0 630 150" aria-hidden="true">
        <polygon points="0,50 65,42 65,130 18,145 40,95" fill="var(--ribbon-dark)"/>
        <polygon points="630,50 565,42 565,130 612,145 590,95" fill="var(--ribbon-dark)"/>
        <polygon points="52,112 65,130 65,110" fill="var(--ribbon-fold)"/>
        <polygon points="578,112 565,130 565,110" fill="var(--ribbon-fold)"/>
        <path d="M52,22 Q315,-4 578,22 L578,112 Q315,86 52,112 Z" fill="var(--ribbon)"/>
        <path d="M60,30 Q315,5 570,30 M60,104 Q315,79 570,104" fill="none" stroke="#f6b36f" stroke-width="2"/>
      </svg>
      <h1>Rooted Together</h1>
    </div>

    <div class="rule rule--top"></div>

    <h2 class="subtitle">
      <span class="count">7 Paths</span>
      <span class="verb">To <em>Raise</em></span>
      <span class="object">A Home That</span>
      <span class="outcome">Flourishes</span>
    </h2>

    <div class="rule rule--bottom"></div>

    <p class="author">Mara Quinlan</p>
  </main>
</body>
</html>
```